ValeHerb.com Cooking Spice Jar Label Design

I need the following labels designed.

dimensions in inches. Drawings attached and logo attached

a. 3.5 oz wrap around spice label 2.3" tall x 3.3" wide
b. 5.5 oz warp around spice label 3.3" tall x 3.6" wide
c. 32 oz clear bottle. Flat label
c. flat label. 2.25 x 4
d. flat front of bottle label 5 x 3.5

Target Market(s)

gourmet cooks. restaurant managers. chefs. grocery store owners.

Industry/Entity Type

Cooking

Font styles to use
Other font styles liked:
• see attached logo

Requirements
Must have
• must be elegant and sophisticated using the existing logo attached.
• please look at www.valeherb.com to see what the 3.5 oz label looks like today with the old logo.
Nice to have

```html
<!DOCTYPE html>
<html lang="en">
<head>
<meta charset="utf-8">
<title>ValeHerb Spice Labels</title>
<link rel="stylesheet" href="https://fonts.googleapis.com/css2?family=Archivo:wght@700;800;900&family=Jost:wght@400&display=swap">
<style>
  :root {
    --bg: #e9e9e7;
    --red-mid: #8e1d1e;
    --red-edge: #5e1012;
    --green-mid: #8d9a2c;
    --green-edge: #5f6a14;
    --silver-light: #f4f4f4;
    --silver-dark: #a9a9a9;
    --ink-light: #ffffff;
    --star-red: #4a0c0d;
    --star-green: #3d4710;
    --netwt: #2b2b2b;
  }
  * { margin: 0; padding: 0; box-sizing: border-box; }
  html, body { width: 1200px; height: 1152px; overflow: hidden; }
  body {
    background: var(--bg);
    position: relative;
  }
  .label {
    position: absolute;
    top: 387px;
    width: 334px;
    height: 546px;
    overflow: hidden;
    color: var(--ink-light);
    text-align: center;
  }
  .label--pepper { left: 213px; background: linear-gradient(90deg, var(--red-edge), var(--red-mid) 25%, var(--red-mid) 75%, var(--red-edge)); }
  .label--ajowan { left: 720px; background: linear-gradient(90deg, var(--green-edge), var(--green-mid) 25%, var(--green-mid) 75%, var(--green-edge)); }

  .label__ornament {
    position: absolute;
    top: 24px;
    bottom: 26px;
    width: 34px;
    background: linear-gradient(90deg, rgba(0,0,0,0.12), rgba(0,0,0,0));
  }
  .label__ornament--left { left: 0; }
  .label__ornament--right { right: 0; transform: scaleX(-1); }

  .label__band {
    position: absolute;
    left: 0; right: 0;
    background: linear-gradient(180deg, var(--silver-light), var(--silver-dark) 55%, var(--silver-light));
  }
  .label__band--top { top: 0; height: 24px; }
  .label__band--bottom { bottom: 0; height: 26px; }
  .label__netwt {
    position: absolute;
    right: 10px;
    bottom: 5px;
    font: 800 14px/1 "Archivo", sans-serif;
    color: var(--netwt);
  }

  .brand {
    position: absolute;
    top: 102px; left: 0; right: 0;
    font: 400 34px/1 "Jost", sans-serif;
    color: var(--ink-light);
  }

  .product {
    position: absolute;
    top: 196px; left: 0; right: 0;
  }
  .product__name {
    font: 900 64px/1 "Archivo", sans-serif;
    letter-spacing: -1px;
  }
  .product__sub {
    margin-top: 6px;
    font: 800 30px/1 "Archivo", sans-serif;
  }

  .label__star {
    position: absolute;
    top: 312px;
    left: 147px;
    width: 40px;
    height: 40px;
  }

  .quality {
    position: absolute;
    top: 364px;
    left: 34px; right: 34px;
    border-top: 2px solid var(--ink-light);
    border-bottom: 2px solid var(--ink-light);
    padding: 8px 0 7px;
    font: 400 28px/1.02 "Jost", sans-serif;
  }
</style>
</head>
<body>

  <section class="label label--pepper">
    <div class="label__ornament label__ornament--left" role="img" aria-label="Dark swirl ornament pattern"></div>
    <div class="label__ornament label__ornament--right" role="img" aria-label="Dark swirl ornament pattern"></div>
    <div class="label__band label__band--top"></div>
    <div class="brand">ValeHerb</div>
    <div class="product">
      <div class="product__name">AFRICAN</div>
      <div class="product__sub">BIRD PEPPER</div>
    </div>
    <svg class="label__star" viewBox="0 0 40 40" aria-hidden="true"><polygon fill="var(--star-red)" points="20,2 24.7,15 38.5,15 27.4,23.3 31.5,37 20,28.8 8.5,37 12.6,23.3 1.5,15 15.3,15"/></svg>
    <div class="quality">QUALITY<br>GOURMET SPICES</div>
    <div class="label__band label__band--bottom"><span class="label__netwt">NET WT 3.5oz</span></div>
  </section>

  <section class="label label--ajowan">
    <div class="label__ornament label__ornament--left" role="img" aria-label="Dark swirl ornament pattern"></div>
    <div class="label__ornament label__ornament--right" role="img" aria-label="Dark swirl ornament pattern"></div>
    <div class="label__band label__band--top"></div>
    <div class="brand">ValeHerb</div>
    <div class="product">
      <div class="product__name">AJOWAN</div>
      <div class="product__sub">PREMIUN</div>
    </div>
    <svg class="label__star" viewBox="0 0 40 40" aria-hidden="true"><polygon fill="var(--star-green)" points="20,2 24.7,15 38.5,15 27.4,23.3 31.5,37 20,28.8 8.5,37 12.6,23.3 1.5,15 15.3,15"/></svg>
    <div class="quality">QUALITY<br>GOURMET SPICES</div>
    <div class="label__band label__band--bottom"><span class="label__netwt">NET WT 3.5oz</span></div>
  </section>

</body>
</html>
```